Employment Agency Website Design

We are working with an employment agency in California.

Some sites to use for content/competitors and inspiration:

https://www.dovelanejobs.example/us/en
https://www.perimowork.example
https://www.tamberlinehire.example
https://www.vintrastaff.example/en
https://www.olmirajobs.example
https://www.quarnstaffing.example

Thank you for taking the time to consider designing a website for us. We are web developers based in Stockton, CA, USA. Most of our projects go through the same process. Understanding this process may help you win a project with us. We custom-code all of our websites in-house. We don’t have any requirements as to what tools you use for your design, but we prefer Figma files. For any design that we label as four-stars, we send it to the client for review. The client picks the final design they want us to use. Once we complete this process, we will continue to show additional clients all the four-star sites and purchase them later. Your designs will have multiple chances to sell. For better chances of success, we ask that you follow these guidelines.

IMAGES:
If you use any images or icons in the design, we ask that you have a link to the asset so we can purchase the image/icon. Most of the designs we submit do not have the customer’s images on them unless they have some great images. Be creative; show us the feeling you are trying to portray with your image choices. Use any royalty-free site you choose. We subscribe to Velsor and mainly use their images, but we can purchase images outside of Velsor. PLEASE NOTE: we will not submit designs to clients with watermarks on the images.

FONTS:
We ask that you identify the fonts used in the design. This can be done in a message if you want. We typically use Google Fonts and Velsor Fonts.

CONTENT:
We're always open to different content and ideas. We often submit designs with stock images so the client can see our vision. We typically take pictures after the website launch to use their images with our vision. Lorem Ipsum is fine for paragraphs, but we ask that you write the headers in correct English. We want to be able to show the vision and identify the sections of the website.

INSPIRATION:
We typically add a couple of links in the brief of websites we like to help you get started in your design.

REVISIONS:
We do not often ask for revisions of the designs unless we see something in the design that may not appeal to the client. If there are slight changes that we want to make, we do that in the development process.

FEEDBACK:
We rarely give feedback on designs during the design process. We are working on many website projects and do not have the time to provide feedback. We usually respond if your request is well thought out and asks specific questions, but a note asking “feedback, please” usually goes unanswered.

```html
<!DOCTYPE html>
<html lang="en">
<head>
<meta charset="utf-8">
<title>Keystead – Helping Good People Find Good Jobs</title>
<link href="https://fonts.googleapis.com/css2?family=PT+Sans:ital,wght@0,400;0,700;1,400&display=swap" rel="stylesheet">
<style>
:root{
  --red:#c01f2f;
  --ink:#111111;
  --text:#555555;
  --muted:#777777;
  --pink:#fde3e7;
  --light:#f3f3f3;
  --footer:#0b0b12;
  --white:#ffffff;
}
*{box-sizing:border-box;margin:0;padding:0}
html,body{width:1200px;height:4055px;overflow:hidden}
body{position:relative;font-family:'PT Sans',sans-serif;color:var(--ink);background:var(--white)}
.abs{position:absolute}
a{color:inherit;text-decoration:none}

/* header */
.login-bar{left:600px;top:0;width:600px;height:36px;background:var(--red);border-bottom-left-radius:14px;display:flex;align-items:center;gap:70px;padding-left:22px;color:#fff;font-size:14px}
.login-bar span{display:flex;align-items:center;gap:10px}
.login-bar i{width:16px;height:16px;border-radius:50%;background:#fff;display:inline-block}
.brand{left:55px;top:30px;font-size:32px;font-weight:700;color:var(--ink);display:flex;align-items:center;gap:10px}
.brand b{width:36px;height:36px;background:var(--red);border-radius:50%;display:inline-block}
.nav{left:509px;top:52px;display:flex;gap:64px;font-size:17px}

/* hero */
.hero{left:0;top:0;width:1200px;height:692px;background:linear-gradient(#f2f2f2,#e4e4e4)}
.hero-photo{left:566px;top:150px;width:634px;height:542px;background:radial-gradient(ellipse at 55% 45%,#f7efe9,#d9d3cf 70%,#e4e4e4)}
.hero h1{left:55px;top:215px;font-size:64px;line-height:1.22;font-weight:700;width:520px}
.hero-copy{left:61px;top:464px;font-size:16px;line-height:1.35;color:var(--text);width:440px}
.btn{display:flex;align-items:center;justify-content:center;font-weight:700;color:#fff}
.btn-red{background:var(--red)}
.btn-dark{background:var(--ink)}
.b1{left:60px;top:535px;width:204px;height:40px;font-size:14px}
.b2{left:288px;top:535px;width:203px;height:40px;font-size:14px}
.search{left:165px;top:656px;width:870px;height:115px;background:#fff;box-shadow:0 30px 60px rgba(0,0,0,.08)}
.field{top:38px;height:39px;background:#ececec;font-size:15px;color:#444;display:flex;align-items:center;padding-left:18px}
.f1{left:32px;width:264px}.f2{left:332px;width:264px}
.find{left:620px;top:37px;width:225px;height:41px;font-size:16px}

/* services */
.svc{width:220px;text-align:center}
.svc svg{display:block;margin:0 auto}
.svc h3{font-size:20px;font-weight:700;margin-top:14px}
.svc p{font-size:9.5px;color:var(--muted);line-height:1.2;margin:6px auto 0;width:180px}
.about h2{font-size:44px;font-weight:700;letter-spacing:.5px}
.about p{font-size:17px;color:var(--text);line-height:1.35;margin-top:14px;width:545px}
.about-btn{left:587px;top:1156px;width:225px;height:43px;font-size:16px}

/* split sections */
.photo-warm{background:linear-gradient(90deg,#5a4636,#8a7260 45%,#d9cbb7)}
.panel-grey{background:var(--light)}
.pink{background:var(--pink)}
.sec-title{font-size:44px;font-weight:700}
.sec-copy{font-size:17px;line-height:1.35;color:var(--text);width:480px}
.tag{width:189px;height:40px;border:2px solid var(--red);color:var(--red);font-size:13px;font-weight:700;display:flex;align-items:center;justify-content:center;background:#fff}
.outline{border:3px solid var(--red);color:var(--red);font-size:27px;font-weight:700;display:flex;align-items:center;justify-content:center;background:#fff}

/* how it works */
.center-title{left:0;width:1200px;text-align:center;font-size:44px;font-weight:700}
.step-num{width:94px;height:94px;border-radius:50%;background:var(--red);color:#fff;font-size:64px;font-weight:700;display:flex;align-items:center;justify-content:center}
.step h4{font-size:21px;font-weight:700}
.step p{font-size:14px;color:var(--muted);line-height:1.2;margin-top:8px;width:270px}

/* stories */
.story{width:447px;height:211px;background:#fff;box-shadow:0 6px 28px rgba(0,0,0,.08);padding:40px 22px 0 22px}
.story h5{font-size:21px;font-weight:400}
.story q{display:block;font-style:italic;font-size:20px;line-height:1.35;color:var(--text);margin-top:6px;width:350px;quotes:none}
.story span{display:block;color:var(--red);font-size:15px;font-weight:700;margin-top:8px}
.story svg{position:absolute;right:20px;top:22px}

/* subscribe */
.subscribe{left:0;top:3458px;width:1200px;height:267px;background:var(--pink)}
.subscribe h2{left:79px;top:88px;font-size:37px;font-weight:700}
.subscribe p{left:89px;top:142px;font-size:17px;color:var(--text);line-height:1.3;width:470px}
.email{left:749px;top:61px;width:381px;height:57px;background:#fff;font-size:17px;color:#666;display:flex;align-items:center;padding-left:28px}
.sub-btn{left:749px;top:140px;width:381px;height:57px;font-size:22px}

/* footer */
.footer{left:0;top:3725px;width:1200px;height:330px;background:var(--footer);color:#fff}
.f-brand{left:99px;top:52px;font-size:30px;font-weight:700;color:#fff;display:flex;align-items:center;gap:10px}
.f-brand b{width:32px;height:32px;border-radius:50%;background:var(--red);display:inline-block}
.f-desc{left:99px;top:118px;font-size:12.5px;line-height:1.5;width:330px}
.social{left:103px;top:180px;display:flex;gap:28px}
.social i{width:13px;height:13px;border-radius:50%;background:#fff;display:block}
.f-col h6{font-size:17px;font-weight:700;letter-spacing:.3px}
.f-col li{list-style:none;font-size:12.5px;margin-top:15px}
.contact li{display:flex;gap:10px;align-items:flex-start;line-height:1.5}
.copy{right:86px;top:288px;font-size:11px}
</style>
</head>
<body>

<section class="hero abs">
  <div class="hero-photo abs" role="img" aria-label="Smiling young woman in a white t-shirt holding a laptop and glasses"></div>
  <h1 class="abs">Helping Good<br>People Find<br>Good Jobs</h1>
  <p class="hero-copy abs">Lorem ipsum dolor sit amet, consectetuer adipiscing elit. Aenean commodo ligula eget dolor. Aenean massa.</p>
  <a class="btn btn-red b1 abs">FIND YOUR NEXT JOB</a>
  <a class="btn btn-dark b2 abs">FIND YOUR NEXT HIRE</a>
</section>

<header>
  <div class="login-bar abs"><span><i></i>Candidate Login</span><span><i></i>Client Login</span></div>
  <div class="brand abs"><b></b>Keystead</div>
  <nav class="nav abs"><a>Talent Seeker</a><a>Employers</a><a>Soltutions</a><a>About Us</a><a>Contact</a></nav>
</header>

<form class="search abs">
  <div class="field f1 abs">Search Keywords</div>
  <div class="field f2 abs">City, Zip Code</div>
  <a class="btn btn-red find abs">FIND A JOB</a>
</form>

<div class="svc abs" style="left:36px;top:873px">
  <svg width="80" height="80" viewBox="0 0 80 80" fill="none" stroke="#c01f2f" stroke-width="2.5"><rect x="18" y="6" width="46" height="64" rx="3"/><circle cx="30" cy="42" r="14"/><circle cx="30" cy="38" r="5"/><path d="M21 50c3-6 15-6 18 0M40 52l12 12M44 30h14M44 38h14M44 46h10M26 14h30"/></svg>
  <h3>Recruitment</h3><p>Lorem ipsum dolor sit amet, consectetur adipiscing elit, sed do eiusmod tempor incididunt.</p>
</div>
<div class="svc abs" style="left:274px;top:873px">
  <svg width="90" height="80" viewBox="0 0 90 80" fill="none" stroke="#c01f2f" stroke-width="2.5"><rect x="6" y="18" width="62" height="46" rx="4"/><path d="M28 18v-8h18v8M6 38h62M22 34v8M52 34v8"/><circle cx="64" cy="44" r="16" fill="#fff"/><circle cx="64" cy="44" r="10"/></svg>
  <h3>Certified Methods</h3><p>Lorem ipsum dolor sit amet, consectetur adipiscing elit, sed do eiusmod tempor incididunt.</p>
</div>
<div class="svc abs" style="left:36px;top:1059px">
  <svg width="96" height="80" viewBox="0 0 96 80" fill="none" stroke="#c01f2f" stroke-width="2.5"><path d="M4 24l16-12 14 10M92 24L76 12 60 18 44 30c-4 4 2 10 6 6l10-8 20 20M20 40l14 14c3 3 7 0 5-3M30 48l12 12c3 3 7-1 5-4M40 56l8 8c3 3 7-1 4-4M80 48l-28 16M4 24l14 18M92 24L78 46"/></svg>
  <h3>Expatriate Services</h3><p>Lorem ipsum dolor sit amet, consectetur adipiscing elit, sed do eiusmod tempor incididunt.</p>
</div>
<div class="svc abs" style="left:274px;top:1059px">
  <svg width="90" height="80" viewBox="0 0 90 80" fill="none" stroke="#c01f2f" stroke-width="2.5"><rect x="6" y="18" width="62" height="46" rx="4"/><path d="M28 18v-8h18v8M6 38h62M22 34v8M52 34v8"/><circle cx="64" cy="44" r="16" fill="#fff"/><circle cx="64" cy="44" r="10"/></svg>
  <h3>Certified Methods</h3><p>Lorem ipsum dolor sit amet, consectetur adipiscing elit, sed do eiusmod tempor incididunt.</p>
</div>

<section class="about abs" style="left:587px;top:895px">
  <h2>ABOUT US</h2>
  <p>Lorem ipsum dolor sit amet, consectetuer adipiscing elit. Aenean commodo ligula eget dolor. Aenean massa. Cum sociis natoque penatibus et magnis dis parturient montes, nascetur ridiculus mus.</p>
  <p>Donec quam felis, ultricies nec, pellentesque eu, pretium quis, sem. Nulla consequat massa quis enim. Donec pede justo, fringilla vel, aliquet nec, vulputate eget, arcu.</p>
</section>
<a class="btn btn-red about-btn abs">FIND YOUR NEXT JOB</a>

<div class="abs photo-warm" style="left:0;top:1271px;width:614px;height:409px" role="img" aria-label="Office team working together at a desk"></div>
<div class="abs panel-grey" style="left:614px;top:1271px;width:586px;height:409px"></div>
<div class="abs pink" style="left:55px;top:1306px;width:610px;height:349px"></div>
<h2 class="abs sec-title" style="left:114px;top:1388px">SPECIALITIES</h2>
<p class="abs sec-copy" style="left:114px;top:1460px">Lorem ipsum dolor sit amet, consectetuer adipiscing elit. Aenean commodo ligula eget dolor. Aenean massa. Cum sociis natoque penatibus et magnis dis parturient montes, nascetur ridiculus mus.</p>
<div class="tag abs" style="left:722px;top:1402px">Finance and Accounting</div>
<div class="tag abs" style="left:934px;top:1402px">Government</div>
<div class="tag abs" style="left:722px;top:1460px">Technology</div>
<div class="tag abs" style="left:934px;top:1460px">Marketing &amp; Creative</div>
<div class="tag abs" style="left:722px;top:1518px">Legal</div>
<div class="tag abs" style="left:934px;top:1518px">Customer Support</div>

<div class="abs photo-warm" style="left:614px;top:1680px;width:586px;height:422px;background:linear-gradient(270deg,#4a3a2e,#8a7260 45%,#d9cbb7)" role="img" aria-label="Employers meeting in a bright office"></div>
<div class="abs pink" style="left:543px;top:1711px;width:613px;height:362px"></div>
<h3 class="abs" style="left:104px;top:1800px;width:360px;text-align:center;font-size:34px;font-weight:400">Ready to Hire</h3>
<a class="outline abs" style="left:104px;top:1872px;width:360px;height:76px">REQUEST STAFFING</a>
<a class="outline abs" style="left:104px;top:1973px;width:360px;height:76px">LEARN MORE</a>
<h2 class="abs sec-title" style="left:613px;top:1802px">EMPLOYERS</h2>
<p class="abs sec-copy" style="left:613px;top:1874px">Lorem ipsum dolor sit amet, consectetuer adipiscing elit. Aenean commodo ligula eget dolor. Aenean massa. Cum sociis natoque penatibus et magnis dis parturient montes, nascetur ridiculus mus.</p>

<div class="abs photo-warm" style="left:0;top:2105px;width:614px;height:404px" role="img" aria-label="Job seeker working on a laptop"></div>
<div class="abs panel-grey" style="left:614px;top:2105px;width:586px;height:404px"></div>
<div class="abs pink" style="left:55px;top:2136px;width:610px;height:350px"></div>
<h2 class="abs sec-title" style="left:114px;top:2218px">JOB SEEKERS</h2>
<p class="abs sec-copy" style="left:114px;top:2290px">Lorem ipsum dolor sit amet, consectetuer adipiscing elit. Aenean commodo ligula eget dolor. Aenean massa. Cum sociis natoque penatibus et magnis dis parturient montes, nascetur ridiculus mus.</p>
<a class="outline abs" style="left:746px;top:2223px;width:360px;height:76px">SIGN UP NOW</a>
<a class="outline abs" style="left:746px;top:2322px;width:360px;height:76px">LEARN MORE</a>

<h2 class="center-title abs" style="top:2606px">HOW IT WORKS</h2>
<div class="step-num abs" style="left:95px;top:2745px">1</div>
<div class="step-num abs" style="left:452px;top:2745px">2</div>
<div class="step-num abs" style="left:820px;top:2745px">3</div>
<div class="step abs" style="left:104px;top:2865px"><h4>Describe Your Need</h4><p>Lorem ipsum dolor sit amet, consectetur adipiscing elit, sed do eiusmod tempor incididunt.</p></div>
<div class="step abs" style="left:461px;top:2865px"><h4>Describe Your Need</h4><p>Lorem ipsum dolor sit amet, consectetur adipiscing elit, sed do eiusmod tempor incididunt.</p></div>
<div class="step abs" style="left:829px;top:2865px"><h4>Describe Your Need</h4><p>Lorem ipsum dolor sit amet, consectetur adipiscing elit, sed do eiusmod tempor incididunt.</p></div>

<h2 class="center-title abs" style="top:3042px">SUCCESS STORIES</h2>
<article class="story abs" style="left:123px;top:3165px">
  <svg width="54" height="46" viewBox="0 0 54 46" fill="#c01f2f"><path d="M0 0h22v26L10 46H2l8-20H0zM30 0h22v26L40 46h-8l8-20H30z"/></svg>
  <h5>John Doe</h5><q>Lorem ipsum dolor sit amet, consectetur adipiscing elit, sed do eiusmod tempor incididunt.</q><span>Sales assistant</span>
</article>
<article class="story abs" style="left:624px;top:3162px;padding-top:46px">
  <svg width="54" height="46" viewBox="0 0 54 46" fill="#c01f2f"><path d="M0 0h22v26L10 46H2l8-20H0zM30 0h22v26L40 46h-8l8-20H30z"/></svg>
  <h5>John Doe</h5><q>Lorem ipsum dolor sit amet, consectetur adipiscing elit, sed do eiusmod tempor incididunt.</q><span>Sales assistant</span>
</article>

<section class="subscribe abs">
  <h2 class="abs">Subscribe to Get Latest Updates</h2>
  <p class="abs">Lorem ipsum dolor sit amet, consectetur adipiscing elit, sed do eiusmod tempor incididunt.</p>
  <div class="email abs">Email Address</div>
  <a class="btn btn-red sub-btn abs">SUBSCRIBE NOW</a>
</section>

<footer class="footer abs">
  <div class="f-brand abs"><b></b>Keystead</div>
  <p class="f-desc abs">Getting an accurate diagnosis can be one of the most impactful experiences that you can have.</p>
  <div class="social abs"><i></i><i></i><i></i><i></i></div>
  <div class="f-col abs" style="left:455px;top:80px"><h6>QUICK LINKS</h6><ul><li>Home</li><li>About Us</li><li>Services</li><li>Contact</li></ul></div>
  <div class="f-col abs" style="left:658px;top:80px"><h6>OTHER PAGES</h6><ul><li>Job Vacancy</li><li>Charity Program</li><li>Privacy &amp; Policy</li><li>Terms of Use</li></ul></div>
  <div class="f-col contact abs" style="left:861px;top:80px;width:260px"><h6>CONTACT INFO</h6><ul>
    <li><svg width="12" height="16" viewBox="0 0 12 16"><path d="M6 0a6 6 0 0 1 6 6c0 4-6 10-6 10S0 10 0 6a6 6 0 0 1 6-6z" fill="#1fb6a0"/><circle cx="6" cy="6" r="2" fill="#0b0b12"/></svg>418 Harbor Row, Stockton, CA – 95202</li>
    <li><svg width="13" height="13" viewBox="0 0 24 24"><path d="M6.6 10.8a15 15 0 0 0 6.6 6.6l2.2-2.2c.3-.3.7-.4 1-.2 1.1.4 2.3.6 3.6.6.6 0 1 .4 1 1V20c0 .6-.4 1-1 1A17 17 0 0 1 3 4c0-.6.4-1 1-1h3.5c.6 0 1 .4 1 1 0 1.3.2 2.5.6 3.6.1.3 0 .7-.2 1z" fill="#1fb6a0"/></svg>+1 209 555 0147</li>
    <li><svg width="13" height="11" viewBox="0 0 13 11" fill="none" stroke="#1fb6a0" stroke-width="1.5"><rect x="1" y="1" width="11" height="9"/><path d="M1 1l5.5 5L12 1"/></svg>contact@domain.com</li>
  </ul></div>
  <div class="copy abs">Copyright © 2021. All rights reserved.</div>
</footer>

</body>
</html>
```